SUMMIT GATHERING 2021. August 20th -22nd.

The Hosts of the conference: Grace Tabernacle-Pastors Ron n Della ( Picture with two persons)

Guest Minister: Bishop Lucinda Okotieno. (Cedar Ridge Awakening)

Venue:
Sealand Gateway Lodgeview. 4817 North 239th Avenue Seattle, WA 98174.

Conference times.
Friday August 20th 6pm-8:30pm
Saturday August 21st. 6pm-8:30pm

Sunday August 22nd 10am-1pm
“ CHURCH RENEWAL GATHERING”

5pm-7:30pm
TWOFOLD SURGE GATHERING.

Target Market(s)

18-55

Industry/Entity Type

Religious/ Entertainment.

Requirements
Must have
• A highlight of the Relaunch service on Sunday August 22nd 5pm-7:30pm.
Nice to have
• Excellent ideas….

```html
<!DOCTYPE html>
<html lang="en">
<head>
<meta charset="utf-8">
<title>Summit Gathering 2021 — Grace Tabernacle</title>
<link rel="stylesheet" href="https://fonts.googleapis.com/css2?family=Montserrat:wght@300;400;500;700;800&family=Poppins:wght@400;600;700&family=Barlow+Semi+Condensed:wght@700&display=swap">
<style>
  :root {
    --ink: #0c0c0c;
    --ink-soft: #1e1e1e;
    --white: #ffffff;
    --paper: #f4f4f4;
    --red: #c8140f;
    --red-text: #e0201a;
    --gold-light: #f3e2a6;
    --gold: #c9a74c;
    --gold-deep: #9c7a2c;
    --url-ink: #2a2a2a;
  }
  * { margin: 0; padding: 0; box-sizing: border-box; }
  html, body { width: 800px; height: 1200px; overflow: hidden; background: var(--paper); }
  .poster {
    position: relative;
    width: 800px;
    height: 1200px;
    font-family: "Montserrat", sans-serif;
    color: var(--white);
    overflow: hidden;
  }
  .poster-body {
    position: absolute; left: 0; top: 0; width: 800px; height: 1106px;
    background: linear-gradient(180deg, #181818 0%, #111 45%, #0b0b0b 100%);
    overflow: hidden;
  }
  .portrait-backdrop {
    position: absolute; left: 320px; top: 0; width: 480px; height: 620px;
    background: radial-gradient(ellipse 45% 55% at 58% 40%, rgba(80,80,80,0.45), rgba(30,30,30,0.2) 60%, rgba(0,0,0,0) 100%);
  }
  .audience-backdrop {
    position: absolute; left: 0; top: 640px; width: 800px; height: 466px;
    background: linear-gradient(180deg, rgba(0,0,0,0) 0%, rgba(70,70,70,0.28) 35%, rgba(40,40,40,0.25) 70%, rgba(10,10,10,0.6) 100%);
  }
  .brand {
    position: absolute; left: 58px; top: 80px;
    display: flex; align-items: center; gap: 12px;
  }
  .brand-square { width: 22px; height: 22px; background: var(--gold); }
  .brand-name {
    font-family: "Montserrat", sans-serif; font-weight: 700; font-size: 22px;
    letter-spacing: 1px; color: var(--gold);
  }
  .title { position: absolute; left: 56px; top: 232px; line-height: 1; }
  .title-lead { font-weight: 400; font-size: 84px; letter-spacing: -2px; display: block; }
  .title-main {
    display: block; margin-top: 12px; font-weight: 800; font-size: 76px; letter-spacing: -1px;
    background: linear-gradient(180deg, var(--gold-light) 0%, var(--gold) 55%, var(--gold-deep) 100%);
    -webkit-background-clip: text; background-clip: text; color: transparent;
  }
  .title-year { display: block; margin-top: 6px; font-weight: 300; font-size: 104px; letter-spacing: -3px; }
  .rule { position: absolute; left: 60px; top: 519px; width: 383px; height: 2px; background: #cfcfcf; }
  .rule-accent { position: absolute; left: 80px; top: 516px; width: 60px; height: 8px; background: var(--red); border-radius: 4px; }
  .section-heading {
    position: absolute; font-family: "Barlow Semi Condensed", sans-serif; font-weight: 700;
    color: var(--red-text); letter-spacing: -0.3px;
  }
  .venue-heading { left: 62px; top: 557px; font-size: 22px; }
  .venue-address { position: absolute; left: 59px; top: 594px; font-size: 16px; line-height: 23px; font-weight: 400; letter-spacing: 0.5px; }
  .highlight {
    position: absolute; left: 410px; top: 562px; width: 336px; height: 78px;
    background: var(--red); padding: 15px 0 0 19px;
    font-family: "Montserrat", sans-serif; font-weight: 700;
  }
  .highlight-title { font-size: 15.5px; letter-spacing: 0.5px; }
  .highlight-detail { margin-top: 9px; font-size: 11.5px; letter-spacing: 0.3px; }
  .highlight-detail .sep { margin: 0 9px; font-weight: 400; }
  .times-heading { left: 58px; top: 659px; font-size: 25px; }
  .schedule { position: absolute; left: 0; top: 700px; width: 800px; height: 80px; }
  .day { position: absolute; top: 0; font-family: "Poppins", sans-serif; line-height: 24px; }
  .day-icon { position: absolute; left: -28px; top: 3px; width: 18px; height: 18px; }
  .day-name { font-family: "Montserrat", sans-serif; font-weight: 400; font-size: 17px; letter-spacing: 0.5px; }
  .day-date, .day-time { font-weight: 700; font-size: 17px; }
  .day-friday { left: 97px; } .day-saturday { left: 296px; } .day-sunday { left: 492px; }
  .divider { position: absolute; top: 4px; height: 70px; border-left: 1.5px dotted #8a8a8a; }
  .divider-one { left: 246px; } .divider-two { left: 443px; }
  .minister { position: absolute; top: 806px; width: 240px; text-align: center; }
  .minister-hosts { left: 62px; } .minister-guest { left: 330px; }
  .minister-photo {
    width: 190px; height: 190px; margin: 0 auto; border-radius: 50%;
    border: 3px solid var(--gold);
  }
  .minister-hosts .minister-photo { background: radial-gradient(circle at 40% 45%, #8a5a4a 0%, #5b2f7a 45%, #c22d9b 100%); }
  .minister-guest .minister-photo { background: radial-gradient(circle at 50% 50%, #6a4a3a 0%, #a8b8b0 55%, #dfe8e4 100%); }
  .minister-role { margin-top: 23px; font-size: 11px; font-weight: 400; letter-spacing: 0.6px; }
  .minister-name { margin-top: 5px; font-size: 15.5px; font-weight: 700; line-height: 21px; letter-spacing: 0.5px; }
  .footer {
    position: absolute; left: 0; top: 1106px; width: 800px; height: 94px; background: var(--paper);
    display: flex; align-items: center; justify-content: center;
  }
  .footer-url { font-family: "Montserrat", sans-serif; font-weight: 400; font-size: 24px; letter-spacing: 2px; color: var(--url-ink); }
</style>
</head>
<body>
<main class="poster">
  <section class="poster-body">
    <div class="portrait-backdrop" role="img" aria-label="Faded portrait of the guest minister"></div>
    <div class="audience-backdrop" role="img" aria-label="Blurred congregation seated in a hall"></div>

    <div class="brand">
      <span class="brand-square"></span>
      <span class="brand-name">GRACE TABERNACLE</span>
    </div>

    <h1 class="title">
      <span class="title-lead">SUMMIT</span>
      <span class="title-main">GATHERING</span>
      <span class="title-year">2021</span>
    </h1>

    <div class="rule"></div>
    <div class="rule-accent"></div>

    <h2 class="section-heading venue-heading">THE LOCATION OF THE EVENT IS:</h2>
    <p class="venue-address">Sealand Gateway Lodgeview. 4817 North<br>239th Avenue Seattle, WA 98174.</p>

    <aside class="highlight">
      <p class="highlight-title">CHURCH RENEWAL GATHERING</p>
      <p class="highlight-detail">5pm-7:30pm<span class="sep">|</span>TWOFOLD SURGE GATHERING</p>
    </aside>

    <h2 class="section-heading times-heading">CONFERENCE TIMES.</h2>

    <div class="schedule">
      <div class="day day-friday">
        <svg class="day-icon" viewBox="0 0 18 18" fill="none" stroke="#fff" stroke-width="1.3"><rect x="1" y="2.5" width="14" height="13" rx="1.5"/><line x1="1" y1="6" x2="15" y2="6"/><line x1="4.5" y1="1" x2="4.5" y2="4"/><line x1="11.5" y1="1" x2="11.5" y2="4"/><circle cx="13.5" cy="13.5" r="3.5" fill="#111"/><polyline points="13.5,12 13.5,13.7 14.8,14.4"/></svg>
        <p class="day-name">FRIDAY</p><p class="day-date">August 20th</p><p class="day-time">6pm-8:30pm</p>
      </div>
      <div class="divider divider-one"></div>
      <div class="day day-saturday">
        <svg class="day-icon" viewBox="0 0 18 18" fill="none" stroke="#fff" stroke-width="1.3"><rect x="1" y="2.5" width="14" height="13" rx="1.5"/><line x1="1" y1="6" x2="15" y2="6"/><line x1="4.5" y1="1" x2="4.5" y2="4"/><line x1="11.5" y1="1" x2="11.5" y2="4"/><circle cx="13.5" cy="13.5" r="3.5" fill="#111"/><polyline points="13.5,12 13.5,13.7 14.8,14.4"/></svg>
        <p class="day-name">SATURDAY</p><p class="day-date">August 21st</p><p class="day-time">6pm-8:30pm</p>
      </div>
      <div class="divider divider-two"></div>
      <div class="day day-sunday">
        <svg class="day-icon" viewBox="0 0 18 18" fill="none" stroke="#fff" stroke-width="1.3"><rect x="1" y="2.5" width="14" height="13" rx="1.5"/><line x1="1" y1="6" x2="15" y2="6"/><line x1="4.5" y1="1" x2="4.5" y2="4"/><line x1="11.5" y1="1" x2="11.5" y2="4"/><circle cx="13.5" cy="13.5" r="3.5" fill="#111"/><polyline points="13.5,12 13.5,13.7 14.8,14.4"/></svg>
        <p class="day-name">SUNDAY</p><p class="day-date">August 22nd</p><p class="day-time">10am-1pm</p>
      </div>
    </div>

    <figure class="minister minister-hosts">
      <div class="minister-photo" role="img" aria-label="Photo of the hosting pastors, Ron and Della"></div>
      <figcaption>
        <p class="minister-role">HOSTS OF THE CONFERENCE</p>
        <p class="minister-name">GRACE TABERNACLE-PASTORS<br>RON N DELLA</p>
      </figcaption>
    </figure>

    <figure class="minister minister-guest">
      <div class="minister-photo" role="img" aria-label="Photo of guest minister Bishop Lucinda Okotieno"></div>
      <figcaption>
        <p class="minister-role">GUEST MINISTER</p>
        <p class="minister-name">BISHOP LUCINDA<br>OKOTIENO</p>
      </figcaption>
    </figure>
  </section>

  <footer class="footer">
    <p class="footer-url">www.gracetabernacl.org</p>
  </footer>
</main>
</body>
</html>
```